Lanterns Over Saltmere - Islamic Book about death, grave and the hereafter

We need a complete redesign of an old book cover. It is a book about death, the grave, the day of judgment, hellfire and paradise. i've attached our old bookcover. you can take new colors and change completly the design. It is up to you!

```html
<!DOCTYPE html>
<html lang="de">
<head>
<meta charset="utf-8">
<title>Lanterns Over Saltmere – Buchcover</title>
<link rel="stylesheet" href="https://fonts.googleapis.com/css2?family=Montserrat:wght@200;300;400;500&display=swap">
<style>
  :root {
    --page-bg: #1c1a17;
    --cover-yellow: #f4c53a;
    --cover-yellow-light: #f8d670;
    --cover-edge: #e9b525;
    --ink: #2a2213;
    --title-white: #fffdf6;
    --feather-white: #fbf8ef;
    --feather-shadow: rgba(170, 120, 20, 0.25);
  }
  html, body {
    margin: 0;
    padding: 0;
    width: 1200px;
    height: 1200px;
    overflow: hidden;
    background: var(--page-bg);
  }
  .canvas {
    width: 1200px;
    height: 1200px;
    display: flex;
    align-items: center;
    justify-content: center;
  }
  .book-cover {
    position: relative;
    width: 793px;
    height: 1120px;
    background: radial-gradient(ellipse 70% 60% at 50% 48%, var(--cover-yellow-light) 0%, var(--cover-yellow) 75%, var(--cover-edge) 100%);
    font-family: "Montserrat", "Helvetica Neue", Arial, sans-serif;
    color: var(--ink);
    text-align: center;
  }
  .author {
    position: absolute;
    top: 88px;
    left: 0;
    right: 0;
    margin: 0;
    font-size: 30px;
    font-weight: 400;
    letter-spacing: 0.12em;
    text-transform: uppercase;
  }
  .title {
    position: absolute;
    top: 166px;
    left: 0;
    right: 0;
    margin: 0;
    font-size: 86px;
    font-weight: 200;
    line-height: 114px;
    letter-spacing: 0.12em;
    color: var(--title-white);
    text-transform: uppercase;
  }
  .title span { display: block; padding-left: 0.12em; }
  .subtitle {
    position: absolute;
    top: 530px;
    left: 0;
    right: 0;
    margin: 0;
    font-size: 27px;
    font-weight: 400;
    letter-spacing: 0.02em;
  }
  .feather {
    position: absolute;
    left: 236px;
    top: 708px;
    width: 320px;
    height: 210px;
  }
  .publisher {
    position: absolute;
    top: 1028px;
    left: 0;
    right: 0;
    margin: 0;
    font-size: 27px;
    font-weight: 400;
    letter-spacing: 0.02em;
  }
</style>
</head>
<body>
  <main class="canvas">
    <section class="book-cover">
      <p class="author">Mira Haddad-Sorel</p>
      <h1 class="title">
        <span>Lanterns</span>
        <span>Over</span>
        <span>Saltmere</span>
      </h1>
      <p class="subtitle">Vom letzten Atem und dem Licht danach</p>
      <svg class="feather" viewBox="0 0 320 210" role="img" aria-label="Eine einzelne weiße Feder, die sanft auf der Fläche liegt">
        <defs>
          <radialGradient id="feather-glow" cx="50%" cy="50%" r="50%">
            <stop offset="0%" stop-color="#fbf8ef"/>
            <stop offset="70%" stop-color="#fbf8ef" stop-opacity="0.85"/>
            <stop offset="100%" stop-color="#fbf8ef" stop-opacity="0"/>
          </radialGradient>
        </defs>
        <ellipse cx="170" cy="178" rx="120" ry="14" fill="var(--feather-shadow)"/>
        <ellipse cx="160" cy="110" rx="150" ry="72" fill="url(#feather-glow)"/>
      </svg>
      <p class="publisher">Haus Saltmere Verlag</p>
    </section>
  </main>
</body>
</html>
```